Visitenkarten-Design für Psychiaterin
Zielgruppe
Dr. med. Monika Haberl, Ärztin, Psychotherapie für Kinder Jugendliche und Erwachsene, spezialisiert auf komplexe Posttraumatische Belastungsstörung, Dissoziative Störungen, Persönlichkeitsstörungen, Bindungsstörungen, LUMO-Mentorin
Das Design soll modern sein, Seriosität Professionalität, Dynamik und Geborgenheit ausstrahlen. Zielgruppe sind Menschen die traumatische Situationen überlebt haben.
Aufgabenstellung
Name, Fachgebiet und Spezialisierung, Telefonnummer, e-Mail
Unter Dateiupload sind Visitenkartenbeispiele die mir gefallen

```html
<!DOCTYPE html>
<html lang="de">
<head>
<meta charset="utf-8">
<title>Visitenkarte Dr. med. Monika Haberl</title>
<link rel="stylesheet" href="https://fonts.googleapis.com/css2?family=Didact+Gothic&family=Mulish:wght@800&display=swap">
<style>
  :root {
    --teal: #5fb4c2;
    --teal-light: #b0dbe0;
    --card: #fdfdfd;
    --ink: #3e4553;
    --page: #ffffff;
  }
  * { margin: 0; padding: 0; box-sizing: border-box; }
  html, body { width: 868px; height: 1200px; overflow: hidden; background: var(--page); }
  body { position: relative; font-family: "Didact Gothic", sans-serif; color: var(--ink); }

  .card {
    position: absolute; left: 14px; width: 806px; height: 520px;
    border-radius: 40px; overflow: hidden; background: var(--card);
    box-shadow: 6px 10px 18px rgba(0,0,0,0.28);
  }
  .card--front { top: 18px; }
  .card--back { top: 635px; }

  .card__band {
    position: absolute; left: 0; top: 0; width: 100%; height: 316px;
    background: linear-gradient(to bottom, var(--teal) 0, var(--teal) 290px, var(--card) 316px);
  }
  .card__visual {
    position: absolute; left: 78px; top: 42px; width: 296px; height: 274px;
    border-radius: 140px 140px 0 0;
    background: linear-gradient(100deg, var(--teal-light) 0%, #eaf5f6 45%, #ffffff 100%);
  }

  .specialties {
    position: absolute; left: 412px; top: 86px; list-style: none;
    font-size: 22px; line-height: 27.3px; color: var(--ink);
  }
  .specialties li { position: relative; padding-left: 21px; }
  .specialties li::before {
    content: ""; position: absolute; left: 2px; top: 11px;
    width: 8px; height: 8px; border-radius: 50%; background: #fff;
  }

  .contact {
    position: absolute; right: 71px; top: 76px; text-align: right;
    font-size: 23px; line-height: 28.5px; color: var(--ink);
  }
  .contact__address { margin-bottom: 13px; }

  .identity { position: absolute; right: 74px; top: 348px; text-align: right; }
  .identity__title { font-size: 33px; line-height: 36px; }
  .identity__name {
    font-family: "Mulish", sans-serif; font-weight: 800;
    font-size: 45px; line-height: 50px; letter-spacing: 0.3px;
  }
  .identity__field { margin-top: 12px; font-size: 23px; line-height: 28px; margin-right: 0; }
  .card__field {
    position: absolute; right: 74px; top: 456px; font-size: 23px; line-height: 28px;
  }
</style>
</head>
<body>

<article class="card card--front">
  <div class="card__band"></div>
  <div class="card__visual" role="img" aria-label="Illustration: Kopfsilhouetten im Profil mit einem Netzwerk aus farbigen Punkten im Kopf"></div>
  <ul class="specialties">
    <li>Komplexe posttraumatische<br>Belastungsstörungen</li>
    <li>Dissoziative Störungen</li>
    <li>Persönlichkeitsstörungen</li>
    <li>Bindungsstörungen</li>
    <li>LUMO-Mentorin</li>
  </ul>
  <div class="identity">
    <p class="identity__title">Dr. med.</p>
    <h1 class="identity__name">Monika Haberl</h1>
  </div>
  <p class="card__field">Psychotherapie für Kinder, Jugendliche und Erwachsene</p>
</article>

<article class="card card--back">
  <div class="card__band"></div>
  <div class="card__visual" role="img" aria-label="Illustration: Kopfsilhouetten im Profil mit einem Netzwerk aus farbigen Punkten im Kopf"></div>
  <address class="contact" style="font-style: normal;">
    <p>Lindenweg 7</p>
    <p class="contact__address">54321 Beispielstadt</p>
    <p>Fon 01234 918273</p>
    <p>Fax 01234 918274</p>
    <p>haberl@praxis-haberl.de</p>
    <p>www.psychotherapie-haberl.de</p>
  </address>
  <div class="identity">
    <p class="identity__title">Dr. med.</p>
    <h2 class="identity__name">Monika Haberl</h2>
  </div>
  <p class="card__field">Psychotherapie für Kinder, Jugendliche und Erwachsene</p>
</article>

</body>
</html>
```